Flash / HTML5 Loading Screen Animation

We need an animation created that we can overlay on top of one of our current screens.

It will be a loading screen that will consistently loop. From the starting point all the way around should last about 5 seconds and then just keep looping.

We are looking for something similar to the attached screen. Feel free to submit something more creative or different.

We will need the animation in 3 formats.
HTML 5 or CSS
Flash
GIF

```html
<!DOCTYPE html>
<html lang="en">
<head>
<meta charset="utf-8">
<title>Please wait</title>
<link rel="stylesheet" href="https://fonts.googleapis.com/css2?family=Arimo:wght@400&display=swap">
<style>
  :root {
    --page-bg: #ffffff;
    --clay-light: #e3a27f;
    --clay-mid: #cf7f58;
    --clay-dark: #a35a3c;
    --ring-light: #9dcf45;
    --ring-dark: #5f9a2a;
    --ring-track: #2f2f2f;
    --spinner: #7a4a33;
    --label: #6e3b25;
  }
  html, body {
    margin: 0;
    width: 1200px;
    height: 920px;
    overflow: hidden;
    background: var(--page-bg);
  }
  .loading-screen {
    position: relative;
    width: 1200px;
    height: 920px;
  }
  .pot-artwork {
    position: absolute;
    left: 270px;
    top: 100px;
    width: 730px;
    height: 760px;
    border-radius: 40px;
    background: linear-gradient(90deg, var(--clay-mid) 0%, var(--clay-light) 22%, var(--clay-mid) 55%, var(--clay-dark) 100%);
  }
  .progress-ring {
    position: absolute;
    left: 485px;
    top: 410px;
    width: 320px;
    height: 320px;
  }
  .progress-sweep {
    transform-origin: 160px 160px;
    animation: sweep 5s linear infinite;
  }
  .spinner {
    transform-origin: 160px 160px;
    animation: spin 1s steps(8) infinite;
  }
  @keyframes sweep { to { transform: rotate(360deg); } }
  @keyframes spin { to { transform: rotate(360deg); } }
  .status-label {
    position: absolute;
    left: 0;
    width: 1200px;
    top: 748px;
    margin: 0;
    text-align: center;
    font-family: "Arimo", Arial, sans-serif;
    font-size: 42px;
    font-weight: 400;
    color: var(--label);
    letter-spacing: 0.5px;
  }
</style>
</head>
<body>
<main class="loading-screen">
  <div class="pot-artwork" role="img" aria-label="Terracotta flower pot with a wide rim"></div>

  <svg class="progress-ring" viewBox="0 0 320 320" aria-hidden="true">
    <defs>
      <linearGradient id="ringGreen" x1="0" y1="0" x2="1" y2="1">
        <stop offset="0" stop-color="var(--ring-light)"/>
        <stop offset="1" stop-color="var(--ring-dark)"/>
      </linearGradient>
    </defs>
    <circle cx="160" cy="160" r="137" fill="none" stroke="url(#ringGreen)" stroke-width="38"/>
    <g class="progress-sweep">
      <path d="M 274 236 A 137 137 0 0 1 236 274" fill="none" stroke="var(--ring-track)" stroke-width="38"/>
    </g>
    <g class="spinner" stroke="var(--spinner)" stroke-width="4" stroke-linecap="round">
      <line x1="160" y1="136" x2="160" y2="146"/>
      <line x1="177" y1="143" x2="170" y2="150"/>
      <line x1="184" y1="160" x2="174" y2="160"/>
      <line x1="177" y1="177" x2="170" y2="170" opacity="0.85"/>
      <line x1="160" y1="184" x2="160" y2="174" opacity="0.7"/>
      <line x1="143" y1="177" x2="150" y2="170" opacity="0.55"/>
      <line x1="136" y1="160" x2="146" y2="160" opacity="0.4"/>
      <line x1="143" y1="143" x2="150" y2="150" opacity="0.25"/>
    </g>
  </svg>

  <p class="status-label">Please wait...</p>
</main>
</body>
</html>
```